DJ Competition Audition Flyer

We are looking for an updated version of last years campaign design. See attached image which captures the style and feel for our target market audience ranging from 18-35 years.
Please leave out any dates and just focus on the title'Velvet Tideline DJ Competition, images, general theme/design.
Eye candy, WOW factor,
Words like BLAZE FM, COMPETITION, DJ and PRIZES should be the main focus
Thanks!
Target Market(s)
18-35 years DJ';s and Electronic Music Producers
Industry/Entity Type
Music Training
Colors
Designer to choose colors to be used in the design.
Requirements
Must have
- Website address, contact number,
- Eye candy, WOW factor,
- Words like BLAZE FM, COMPETITION, DJ and PRIZES should be the main focus
Should not have
- Any dates

```html
<!DOCTYPE html>
<html lang="en">
<head>
<meta charset="utf-8">
<title>Velvet Tideline DJ Competition – Auditions Now Open</title>
<link rel="stylesheet" href="https://fonts.googleapis.com/css2?family=Anton&family=Bebas+Neue&family=Caveat+Brush&family=Fjalla+One&family=Quicksand:wght@300;400;500&display=swap">
<style>
  :root {
    --orange: #f7a034;
    --magenta: #e9287f;
    --purple: #7a3aa6;
    --indigo: #4b3f9e;
    --navy: #34306f;
    --gold-dark: #b8862a;
    --gold: #e9bd4a;
    --gold-light: #fff0a0;
    --yellow: #fff200;
    --white: #ffffff;
  }
  * { box-sizing: border-box; margin: 0; padding: 0; }
  html, body { width: 927px; height: 1200px; overflow: hidden; }
  body { background: var(--navy); }
  .flyer {
    position: relative; width: 927px; height: 1200px; overflow: hidden;
    color: var(--white);
  }
  .backdrop {
    position: absolute; inset: 0;
    background: linear-gradient(172deg, var(--orange) 0%, #f46a4e 22%, var(--magenta) 45%, #b936a0 68%, var(--purple) 82%, var(--indigo) 100%);
  }
  .abs { position: absolute; }
  .headline-script {
    left: 0; width: 927px; top: 70px; text-align: center;
    font-family: "Caveat Brush", cursive; font-size: 96px; line-height: 1; font-weight: 400;
    text-shadow: 3px 4px 4px rgba(90, 20, 40, .45);
  }
  .frame { position: absolute; inset: 0; }
  .title {
    left: 0; width: 927px; top: 274px; text-align: center;
    font-family: "Anton", sans-serif; font-size: 82px; line-height: 92px; font-weight: 400;
    letter-spacing: -1px; text-transform: uppercase;
    text-shadow: 4px 6px 6px rgba(80, 10, 60, .45);
  }
  .ribbon { position: absolute; inset: 0; }
  .prizes-tag {
    left: 0; width: 927px; top: 492px; text-align: center;
    font-family: "Anton", sans-serif; font-size: 34px; line-height: 40px; color: #1c1230;
  }
  .prize-main {
    left: 0; width: 927px; top: 548px; text-align: center;
    font-family: "Fjalla One", sans-serif; font-size: 44px; line-height: 54px; letter-spacing: -1px;
  }
  .prize-main .pink { color: #f02f8c; }
  .prize-main .orange { color: #f8a13a; }
  .prize-main .station { color: var(--white); font-family: "Anton", sans-serif; letter-spacing: 0; }
  .prize-sub {
    left: 0; width: 927px; top: 598px; text-align: center;
    font-family: "Quicksand", sans-serif; font-weight: 400; font-size: 30px; line-height: 36px;
  }
  .prize-gigs {
    left: 0; width: 927px; top: 652px; text-align: center;
    font-family: "Quicksand", sans-serif; font-weight: 400; font-size: 62px; line-height: 70px;
    background: linear-gradient(180deg, var(--gold-light), var(--gold) 55%, var(--gold-dark));
    -webkit-background-clip: text; background-clip: text; color: transparent;
  }
  .prize-more {
    left: 0; width: 927px; top: 718px; text-align: center;
    font-family: "Fjalla One", sans-serif; font-size: 50px; line-height: 60px; color: var(--yellow); letter-spacing: -1px;
  }
  .judges {
    left: 0; width: 927px; top: 812px;
    display: flex; justify-content: center; align-items: center; gap: 22px;
  }
  .judges-label {
    font-family: "Anton", sans-serif; font-size: 54px; line-height: 62px; letter-spacing: -1px; font-weight: 400;
    background: linear-gradient(180deg, var(--gold-light), var(--gold) 50%, var(--gold-dark));
    -webkit-background-clip: text; background-clip: text; color: transparent;
  }
  .judges-names {
    font-family: "Bebas Neue", sans-serif; font-size: 30px; line-height: 30px;
  }
  .judges-names .crew { font-size: 12px; color: var(--yellow); vertical-align: top; margin-left: 6px; }
  .venue-tag {
    left: 80px; top: 1034px; width: 104px; height: 17px; padding-left: 8px;
    font-family: "Quicksand", sans-serif; font-size: 12px; line-height: 17px; color: #3b2a10;
    background: linear-gradient(90deg, var(--gold-dark), var(--gold-light), var(--gold));
    clip-path: polygon(0 0, 100% 0, 94% 50%, 100% 100%, 0 100%, 5% 50%);
  }
  .venue {
    left: 87px; top: 1055px; font-style: normal;
    font-family: "Quicksand", sans-serif; font-size: 12.5px; line-height: 17px;
  }
  .book-tag {
    left: 309px; top: 1008px; width: 236px; height: 28px; padding-left: 10px;
    font-family: "Quicksand", sans-serif; font-weight: 500; font-size: 20px; line-height: 28px; color: #2c2210;
    background: linear-gradient(90deg, var(--gold-dark), var(--gold-light) 45%, var(--gold));
    clip-path: polygon(0 0, 100% 0, 95% 50%, 100% 100%, 0 100%, 3% 50%);
  }
  .website {
    left: 318px; top: 1042px;
    font-family: "Quicksand", sans-serif; font-size: 25px; line-height: 32px;
  }
  .phone {
    left: 316px; top: 1074px;
    font-family: "Quicksand", sans-serif; font-weight: 400; font-size: 46px; line-height: 56px;
  }
  .school-name {
    left: 690px; top: 1052px; width: 180px;
    display: flex; align-items: center; gap: 10px;
    font-family: "Quicksand", sans-serif; font-weight: 500; font-size: 16px; line-height: 19px;
  }
  .school-name .dot { flex: none; width: 38px; height: 38px; border-radius: 50%; background: #1b1740; }
</style>
</head>
<body>
<main class="flyer">

  <div class="backdrop" role="img" aria-label="Decorative background of diagonal rounded streaks and circles in orange, pink and violet"></div>

  <h2 class="abs headline-script">Auditions Now Open</h2>

  <svg class="frame" width="927" height="1200" viewBox="0 0 927 1200" aria-hidden="true">
    <defs>
      <linearGradient id="goldFrame" x1="0" y1="0" x2="1" y2="1">
        <stop offset="0" stop-color="#fff0a0"/><stop offset=".4" stop-color="#c9962b"/>
        <stop offset=".7" stop-color="#ffe27a"/><stop offset="1" stop-color="#b8862a"/>
      </linearGradient>
    </defs>
    <rect x="161" y="233" width="606" height="670" fill="none" stroke="url(#goldFrame)" stroke-width="7"/>
  </svg>

  <h1 class="abs title">Velvet Tideline<br>DJ Competition</h1>

  <svg class="ribbon" width="927" height="1200" viewBox="0 0 927 1200" aria-hidden="true">
    <defs>
      <linearGradient id="ribbonFill" x1="0" y1="0" x2="1" y2="1">
        <stop offset="0" stop-color="#2c2c66"/><stop offset=".5" stop-color="#5a2f86"/><stop offset="1" stop-color="#d23a86"/>
      </linearGradient>
      <linearGradient id="tagGold" x1="0" y1="0" x2="1" y2="0">
        <stop offset="0" stop-color="#b8862a"/><stop offset=".5" stop-color="#fff0a0"/><stop offset="1" stop-color="#c9962b"/>
      </linearGradient>
      <linearGradient id="lineFade" x1="0" y1="0" x2="1" y2="0">
        <stop offset="0" stop-color="#7a5cd0" stop-opacity="0"/><stop offset="1" stop-color="#9a6ae0"/>
      </linearGradient>
      <linearGradient id="lineFadeR" x1="0" y1="0" x2="1" y2="0">
        <stop offset="0" stop-color="#f05aa0"/><stop offset="1" stop-color="#f05aa0" stop-opacity="0"/>
      </linearGradient>
    </defs>
    <polygon fill="url(#ribbonFill)" points="
      110,512 820,512
      834,529 820,547 834,564 820,582 834,599 820,617 834,634 820,651 834,669 820,686 834,703 820,721 834,738 820,756 834,773 820,790
      110,790
      94,773 110,756 94,738 110,721 94,703 110,686 94,669 110,651 94,634 110,617 94,599 110,582 94,564 110,547 94,529"/>
    <polygon fill="url(#tagGold)" points="368,490 552,490 546,512 552,534 374,534 368,512"/>
    <g stroke-linecap="round">
      <line x1="150" y1="670" x2="330" y2="670" stroke="url(#lineFade)" stroke-width="4"/>
      <line x1="176" y1="680" x2="330" y2="680" stroke="url(#lineFade)" stroke-width="5"/>
      <line x1="190" y1="690" x2="330" y2="690" stroke="url(#lineFade)" stroke-width="4"/>
      <line x1="210" y1="700" x2="330" y2="700" stroke="url(#lineFade)" stroke-width="3"/>
      <line x1="598" y1="670" x2="766" y2="670" stroke="url(#lineFadeR)" stroke-width="4"/>
      <line x1="598" y1="680" x2="740" y2="680" stroke="url(#lineFadeR)" stroke-width="5"/>
      <line x1="598" y1="690" x2="730" y2="690" stroke="url(#lineFadeR)" stroke-width="4"/>
      <line x1="598" y1="700" x2="710" y2="700" stroke="url(#lineFadeR)" stroke-width="3"/>
    </g>
  </svg>

  <div class="abs prizes-tag">PRIZES</div>
  <p class="abs prize-main"><span class="pink">Exclusive Interview &amp;</span> <span class="orange">Airplay on</span> <span class="station">BLAZE FM</span></p>
  <p class="abs prize-sub">Online Feature Interview on Soundwire Magazine</p>
  <p class="abs prize-gigs">Live Gigs</p>
  <p class="abs prize-more">Mentoring, Recording + Heaps More!</p>

  <div class="abs judges">
    <div class="judges-label">JUDGES</div>
    <p class="judges-names">Nadia K, Tess Marlow,<br>Leon Varga<span class="crew">KORRIN</span></p>
  </div>

  <div class="abs venue-tag">Auditions Held at</div>
  <address class="abs venue">Studio 12 @<br>MERIDIAN SCHOOL OF MUSIC<br>Level 2, B4, Harbour St Eastvale</address>

  <div class="abs book-tag">Book your Audition at</div>
  <p class="abs website">meridianschoolofmusic.com.au</p>
  <p class="abs phone">(03) 9412 7763</p>

  <div class="abs school-name"><span class="dot"></span><span>MERIDIAN SCHOOL OF MUSIC</span></div>

</main>
</body>
</html>
```